Help create retail shipping website

We need a Squarespace design for our company Tandem Parcel. We are a retail shipping service that offers mailboxes, shipping, notary, and printing services. This store is similar to a KWB store, BoxVane, and Ridgeway Mailhouse. We would like to have help designing our website. I will provide our logo for the website. I would like our website to be professional, but be very inviting.

```html
<!DOCTYPE html>
<html lang="en">
<head>
<meta charset="utf-8">
<title>Tandem Parcel — Mailboxes, Shipping, Notary</title>
<link href="https://fonts.googleapis.com/css2?family=Montserrat:wght@400;500;600;700;800&display=swap" rel="stylesheet">
<style>
:root{
  --red:#dc0a0a;
  --ink:#1c1f27;
  --dark:#1d2029;
  --text:#444a55;
  --muted:#6b707a;
  --grey:#f0f0f0;
  --line:#d9d9d9;
  --white:#ffffff;
}
*{box-sizing:border-box;margin:0;padding:0}
html,body{width:1200px;height:4310px;overflow:hidden}
body{position:relative;font-family:"Montserrat",Arial,sans-serif;color:var(--ink);background:var(--white)}
.abs{position:absolute}
.btn{position:absolute;display:flex;align-items:center;justify-content:center;font-size:13px;font-weight:500;color:var(--white);background:var(--red);border-radius:2px}
.btn.dark{background:var(--ink)}
.h2{position:absolute;font-size:31px;font-weight:800;text-transform:uppercase;letter-spacing:-.2px;line-height:1.25}
.h2 .accent{color:var(--red)}
.para{position:absolute;font-size:12px;line-height:23px;color:var(--text)}
.photo{position:absolute;border-radius:14px}

/* top bar & nav */
.topbar{left:0;top:0;width:1200px;height:47px;background:var(--dark)}
.brand-panel{left:0;top:0;width:410px;height:117px;background:var(--red);clip-path:polygon(0 0,100% 0,93% 100%,0 100%)}
.brand{position:absolute;left:72px;top:38px;color:var(--white)}
.brand .name{font-size:23px;font-weight:800;letter-spacing:.3px;display:flex;align-items:center;gap:10px}
.brand .dot{width:18px;height:18px;background:var(--white);border-radius:50%}
.brand .tag{font-size:8.5px;letter-spacing:2.2px;margin-top:2px;padding-left:28px;font-weight:500}
.socials{left:425px;top:14px;display:flex;gap:14px}
.socials span{width:18px;height:18px;border:2px solid var(--white);border-radius:4px}
.contact-top{top:16px;font-size:12.5px;color:var(--white);display:flex;align-items:center;gap:9px}
.nav{left:427px;top:73px;display:flex;gap:22px;font-size:11.5px;font-weight:500;color:var(--ink)}
.nav .active{color:var(--red)}
.find-store{left:1001px;top:62px;width:128px;height:40px;font-size:11.5px;font-weight:700}

/* hero */
.hero{left:0;top:117px;width:1200px;height:487px;background:linear-gradient(90deg,#2b2d33 0%,#4a4d54 45%,#8a8c90 80%,#6d7075 100%)}
.hero h1{position:absolute;left:142px;top:236px;font-size:35px;line-height:47px;font-weight:700;color:var(--white);text-transform:uppercase}
.hero p{position:absolute;left:142px;top:353px;width:390px;font-size:13.5px;line-height:23px;color:var(--white)}
.arrow-circle{position:absolute;width:44px;height:44px;border-radius:50%;background:rgba(255,255,255,.18);display:flex;align-items:center;justify-content:center}
.dots{left:565px;top:565px;display:flex;gap:12px}
.dots span{width:9px;height:9px;border-radius:50%;background:rgba(255,255,255,.45)}
.dots .on{background:var(--white)}

/* services */
.service-card{position:absolute;top:830px;width:218px;height:270px;background:var(--white);box-shadow:0 4px 16px rgba(0,0,0,.09)}
.service-card .img{height:206px;border-bottom:3px solid var(--red)}
.service-card .label{display:flex;align-items:center;gap:12px;padding:18px 14px;font-size:15px;font-weight:500}

/* about */
.about-bg{left:0;top:1255px;width:1200px;height:662px;background:var(--grey)}
.framed{position:absolute;border:7px solid var(--white);border-radius:8px}

/* estimate form */
.field-label{position:absolute;font-size:10px;font-weight:500}
.field{position:absolute;left:142px;width:302px;height:35px;border:1px solid var(--line);border-radius:3px;background:var(--white);display:flex;align-items:center;font-size:12px;color:#9a9ea6}
.field .ico{width:27px;height:27px;margin:0 10px 0 4px;background:var(--red);border-radius:3px}

/* why */
.why-bg{left:0;top:2478px;width:1200px;height:560px;background:var(--grey)}
.check{position:absolute;left:646px;display:flex;align-items:center;gap:10px;font-size:12px;font-weight:500}

/* news */
.news-card{position:absolute;top:3214px;width:282px;height:337px;background:var(--white);border-radius:8px;box-shadow:0 4px 16px rgba(0,0,0,.09);overflow:hidden}
.news-card .img{height:184px;position:relative}
.news-card .date{position:absolute;right:0;bottom:0;background:var(--dark);color:var(--white);font-size:10.5px;padding:8px 14px;border-radius:8px 0 0 0}
.news-card h3{font-size:12.5px;font-weight:700;line-height:20px;padding:18px 18px 6px}
.news-card p{font-size:11px;line-height:18px;color:var(--muted);padding:0 18px}
.news-card a{display:block;font-size:11px;font-weight:700;color:var(--red);text-decoration:underline;padding:12px 18px}
.side-arrow{position:absolute;width:38px;height:38px;border-radius:50%;background:var(--white);box-shadow:0 2px 10px rgba(0,0,0,.15);display:flex;align-items:center;justify-content:center}

/* newsletter & footer */
.footer{left:0;top:3925px;width:1200px;height:385px;background:var(--dark)}
.newsletter{left:142px;top:3708px;width:916px;height:256px;background:var(--red);border-radius:14px}
.footer-col{position:absolute;top:4020px;color:var(--white)}
.footer-col h4{font-size:15px;font-weight:800;text-transform:uppercase;margin-bottom:12px}
.footer-col h4 .accent{color:var(--red)}
.footer-col li{list-style:none;font-size:11.5px;line-height:25px}
.foot-social{left:142px;top:4100px;display:flex;gap:10px}
.foot-social span{width:26px;height:26px;background:var(--white);border-radius:3px}
.contact-row{display:flex;gap:14px;font-size:11.5px;line-height:19px;margin-bottom:16px}
.copyright{left:0;top:4279px;width:1200px;text-align:center;font-size:11px;color:#c9ccd3}
</style>
</head>
<body>

<!-- header -->
<div class="abs topbar"></div>
<div class="abs socials"><span></span><span></span><span></span><span></span></div>
<div class="abs contact-top" style="left:773px">
  <svg width="16" height="12" viewBox="0 0 16 12"><rect width="16" height="12" rx="1.5" fill="#dc0a0a"/><path d="M1 1l7 6 7-6" stroke="#fff" stroke-width="1.4" fill="none"/></svg>
  info@tandemparcel.com
</div>
<div class="abs contact-top" style="left:1018px">
  <svg width="15" height="15" viewBox="0 0 24 24"><path d="M6.6 10.8a15 15 0 006.6 6.6l2.2-2.2c.3-.3.7-.4 1-.2 1.1.4 2.3.6 3.6.6.6 0 1 .4 1 1V20c0 .6-.4 1-1 1A17 17 0 013 4c0-.6.4-1 1-1h3.5c.6 0 1 .4 1 1 0 1.3.2 2.5.6 3.6.1.3 0 .7-.2 1z" fill="#dc0a0a"/></svg>
  123-456-7890
</div>
<div class="abs brand-panel">
  <div class="brand">
    <div class="name"><span class="dot"></span>TANDEM PARCEL</div>
    <div class="tag">MAILBOXES | SHIPPING | NOTARY</div>
  </div>
</div>
<nav class="abs nav">
  <span class="active">HOME</span><span>ABOUT US</span><span>SERVICES</span><span>ESTIMATES</span><span>NEWS</span><span>LOCATIONS</span><span>CONTACT US</span>
</nav>
<div class="btn find-store">FIND A STORE</div>

<!-- hero -->
<section class="abs hero" role="img" aria-label="Delivery van loaded with cardboard parcels at a warehouse loading dock"></section>
<h1 class="abs" style="left:142px;top:236px;font-size:35px;line-height:47px;font-weight:700;color:#fff">FAST, RELIABLE, AND<br>HASSLE-FREE SHIPPING</h1>
<p class="abs" style="left:142px;top:353px;width:390px;font-size:13.5px;line-height:23px;color:#fff">It Is A Long Established Fact That A Reader Will Be Distracted By The Readable Content Of A Page When Looking At Its Layout.</p>
<div class="btn" style="left:142px;top:449px;width:124px;height:40px;font-size:11px;font-weight:700">CONTACT US</div>
<div class="abs" style="left:290px;top:449px;display:flex;align-items:center;gap:10px;color:#fff;font-size:13px;font-weight:500">
  <svg width="40" height="40" viewBox="0 0 40 40"><circle cx="20" cy="20" r="20" fill="#fff"/><path d="M16 12l12 8-12 8z" fill="#1c1f27"/></svg>
  Watch Now
</div>
<div class="arrow-circle" style="left:44px;top:338px"><svg width="26" height="12" viewBox="0 0 26 12"><path d="M25 6H2M7 1L2 6l5 5" stroke="#fff" stroke-width="1.6" fill="none"/></svg></div>
<div class="arrow-circle" style="left:1112px;top:338px"><svg width="26" height="12" viewBox="0 0 26 12"><path d="M1 6h23M19 1l5 5-5 5" stroke="#fff" stroke-width="1.6" fill="none"/></svg></div>
<div class="abs dots"><span></span><span class="on"></span><span></span><span></span></div>

<!-- services -->
<h2 class="h2" style="left:0;width:1200px;text-align:center;top:712px"><span class="accent">RETAIL</span> SHIPPING SERVICES</h2>
<p class="para" style="left:160px;width:880px;top:760px;text-align:center">Lorem ipsum dolor sit amet, consectetur adipiscing elit, sed do eiusmod tempor incididunt ut labore et dolore magna aliqua. Ut enim ad minim veniam, quis nostrud exercitation ullamco laboris nisi ut aliquip ex ea commodo consequat.</p>
<div class="service-card" style="left:142px">
  <div class="img" role="img" aria-label="Red mailbox beside a brick wall" style="background:linear-gradient(160deg,#c9b8ab,#b82b2b 60%,#8c5a3a)"></div>
  <div class="label"><svg width="38" height="30" viewBox="0 0 38 30"><rect x="8" y="6" width="22" height="13" rx="6" fill="none" stroke="#1c1f27" stroke-width="1.6"/><path d="M19 19v10M14 29h10" stroke="#1c1f27" stroke-width="1.6"/><path d="M26 3v8" stroke="#dc0a0a" stroke-width="2"/><path d="M1 10h5M2 14h4" stroke="#dc0a0a" stroke-width="1.6"/></svg>Mailboxes</div>
</div>
<div class="service-card" style="left:374px">
  <div class="img" role="img" aria-label="Two couriers unloading boxes from a van" style="background:linear-gradient(160deg,#8d939b,#3d5a86 55%,#c9a27a)"></div>
  <div class="label"><svg width="44" height="28" viewBox="0 0 44 28"><path d="M12 4h18v16H12zM30 10h7l5 6v4H30z" fill="none" stroke="#1c1f27" stroke-width="1.6"/><circle cx="17" cy="22" r="3" fill="#fff" stroke="#1c1f27" stroke-width="1.6"/><circle cx="35" cy="22" r="3" fill="#fff" stroke="#1c1f27" stroke-width="1.6"/><path d="M1 9h8M3 13h6M1 17h8" stroke="#dc0a0a" stroke-width="1.6"/></svg>Shipping</div>
</div>
<div class="service-card" style="left:607px">
  <div class="img" role="img" aria-label="Hand sealing a document with a wax stamp" style="background:linear-gradient(160deg,#d9dce2,#efe8e2 55%,#c99a8c)"></div>
  <div class="label"><svg width="36" height="32" viewBox="0 0 36 32"><rect x="4" y="2" width="20" height="26" rx="2" fill="none" stroke="#1c1f27" stroke-width="1.6"/><path d="M8 9h12M8 14h8" stroke="#1c1f27" stroke-width="1.6"/><circle cx="26" cy="22" r="6" fill="none" stroke="#dc0a0a" stroke-width="1.8"/></svg>Notary</div>
</div>
<div class="service-card" style="left:840px">
  <div class="img" role="img" aria-label="Large format printer producing a colourful print" style="background:linear-gradient(160deg,#d8d8d8,#6a7080 45%,#c45a2a 75%,#1c1f27)"></div>
  <div class="label"><svg width="38" height="32" viewBox="0 0 38 32"><rect x="3" y="10" width="32" height="14" rx="2" fill="none" stroke="#1c1f27" stroke-width="1.6"/><path d="M10 10V3h18v7M10 20h18v10H10z" fill="#fff" stroke="#1c1f27" stroke-width="1.6"/><path d="M14 24h10M14 27h8" stroke="#dc0a0a" stroke-width="1.4"/></svg>Printing Services</div>
</div>
<div class="btn" style="left:536px;top:1128px;width:127px;height:42px">Contact Us</div>

<!-- about -->
<div class="abs about-bg"></div>
<div class="photo" role="img" aria-label="Warehouse manager and worker reviewing a tablet" style="left:142px;top:1359px;width:365px;height:390px;background:linear-gradient(150deg,#d7d2c9,#8e8a7d 45%,#9bb53a 75%,#3c3f42)"></div>
<div class="framed" style="left:365px;top:1590px;width:219px;height:238px">
  <div role="img" aria-label="Worker carrying a box between warehouse shelves" style="width:100%;height:100%;border-radius:4px;background:linear-gradient(160deg,#c9b59a,#6f5c4a 55%,#b4392b)"></div>
</div>
<div class="abs" style="left:146px;top:1778px;color:#8a8d93">
  <div style="font-size:23px;font-weight:800">TANDEM PARCEL</div>
  <div style="font-size:8px;letter-spacing:2.2px;font-weight:500">MAILBOXES | SHIPPING | NOTARY</div>
</div>
<h2 class="h2" style="left:646px;top:1382px"><span class="accent">ABOUT</span> TANDEM PARCEL</h2>
<p class="para" style="left:646px;top:1430px;width:412px">Lorem ipsum dolor sit amet, consectetur adipiscing elit, sed do ex eiusmod tempor incididunt ut labore et dolore magna aliqua. Ut et enim ad minim veniam, quis nostrud exercitation.</p>
<p class="para" style="left:646px;top:1506px;width:412px">Ut aliquip ex ea commodo consequat duis aute irure dolor in amet reprehenderit in voluptate velit esse cillum dolore eu fugiat nulla ut pariatur. Excepteur sint occaecat cupidatat non proident, sunt in a culpa qui officia deserunt mollit anim id est laborum amet.</p>
<p class="para" style="left:646px;top:1605px;width:412px">Sed ut perspiciatis unde omnis iste natus error sit voluptatem dolor accusantium doloremque laudantium, totam rem aperiam, eaque ut ipsa quae ab illo inventore veritatis et quasi architecto beatae ex ea vitae dicta sunt explicabo sed do eiusmod tempor.</p>
<div class="btn" style="left:646px;top:1721px;width:127px;height:42px">Contact Us</div>
<div class="btn dark" style="left:787px;top:1721px;width:128px;height:42px">Read More</div>

<!-- estimate -->
<h2 class="h2" style="left:142px;top:2020px"><span class="accent">GET</span> A FREE SHIPPING<br>ESTIMATE</h2>
<p class="para" style="left:142px;top:2110px;width:420px">Lorem ipsum dolor sit amet, consectetur adipiscing elit, sed do amet eiusmod tempor incididunt ut labore et dolore magna aliqua.</p>
<div class="field-label" style="left:145px;top:2167px">Origin</div>
<div class="field" style="top:2188px"><span class="ico"></span>ZIP Code</div>
<div class="field-label" style="left:145px;top:2239px">Destination</div>
<div class="field" style="top:2260px"><span class="ico"></span>ZIP Code</div>
<div class="btn dark" style="left:142px;top:2323px;width:126px;height:41px">Submit</div>
<div class="photo" role="img" aria-label="Two store staff packing a parcel in a stockroom" style="left:629px;top:2002px;width:429px;height:390px;background:linear-gradient(140deg,#e6e4e0,#6aa2d4 40%,#2d4e7a 65%,#c49a6c)"></div>

<!-- why choose us -->
<div class="abs why-bg"></div>
<div class="photo" role="img" aria-label="Two warehouse workers in hard hats checking a parcel" style="left:142px;top:2563px;width:429px;height:390px;background:linear-gradient(150deg,#b9a48a,#e0782a 45%,#5e4836 80%)"></div>
<h2 class="h2" style="left:646px;top:2614px"><span class="accent">WHY</span> CHOOSE US</h2>
<p class="para" style="left:646px;top:2663px;width:415px">Lorem ipsum dolor sit amet, consectetur adipiscing elit, sed do amet eiusmod tempor incididunt ut labore et dolore magna aliqua. Ut do enim ad minim veniam, quis nostrud exercitation ullamco laboris</p>
<div class="check" style="top:2744px"><svg width="18" height="18" viewBox="0 0 18 18"><circle cx="9" cy="9" r="9" fill="#dc0a0a"/><path d="M5 9l3 3 5-6" stroke="#fff" stroke-width="2" fill="none"/></svg>We Ship 35,000 Parcels Every Year.</div>
<div class="check" style="top:2775px"><svg width="18" height="18" viewBox="0 0 18 18"><circle cx="9" cy="9" r="9" fill="#dc0a0a"/><path d="M5 9l3 3 5-6" stroke="#fff" stroke-width="2" fill="none"/></svg>Lorem Ipsum Dolor Sit Amet, Consectetur Adipiscing Elit.</div>
<div class="check" style="top:2806px"><svg width="18" height="18" viewBox="0 0 18 18"><circle cx="9" cy="9" r="9" fill="#dc0a0a"/><path d="M5 9l3 3 5-6" stroke="#fff" stroke-width="2" fill="none"/></svg>Lorem Ipsum Dolor Sit Amet, Consectetur Adipiscing Elit.</div>
<div class="btn" style="left:646px;top:2854px;width:127px;height:41px">Contact Us</div>

<!-- news -->
<h2 class="h2" style="left:0;width:1200px;text-align:center;top:3118px"><span class="accent">RECENT</span> NEWS</h2>
<p class="para" style="left:0;width:1200px;text-align:center;top:3166px">Lorem ipsum dolor sit amet, consectetur adipiscing elit, sed do eiusmod tempor incididunt ut labore et dolore magna aliqua.</p>
<div class="side-arrow" style="left:76px;top:3364px"><svg width="10" height="14" viewBox="0 0 10 14"><path d="M8 1L2 7l6 6" stroke="#1c1f27" stroke-width="2" fill="none"/></svg></div>
<div class="side-arrow" style="left:1086px;top:3364px"><svg width="10" height="14" viewBox="0 0 10 14"><path d="M2 1l6 6-6 6" stroke="#1c1f27" stroke-width="2" fill="none"/></svg></div>
<article class="news-card" style="left:142px">
  <div class="img" role="img" aria-label="Couriers loading parcels into a van" style="background:linear-gradient(150deg,#c4c7cc,#3f5f93 50%,#b58a5f)"><span class="date">23 May, 2024</span></div>
  <h3>Lorem Ipsum is simply dummy text of the printing and typesetting...</h3>
  <p>It is a long established fact that a reader will be distracted by the readable content...</p>
  <a>Read More</a>
</article>
<article class="news-card" style="left:459px">
  <div class="img" role="img" aria-label="Hand pressing a wax seal onto paper" style="background:linear-gradient(150deg,#e4e2df,#d7c7bd 55%,#b8404a)"><span class="date">5 June, 2024</span></div>
  <h3>Lorem Ipsum is simply dummy text of the printing and typesetting...</h3>
  <p>It is a long established fact that a reader will be distracted by the readable content...</p>
  <a>Read More</a>
</article>
<article class="news-card" style="left:776px">
  <div class="img" role="img" aria-label="Worker checking stock in a warehouse aisle" style="background:linear-gradient(150deg,#cbb89c,#7d6a55 55%,#a83a2e)"><span class="date">10 June, 2024</span></div>
  <h3>Lorem Ipsum is simply dummy text of the printing and typesetting...</h3>
  <p>It is a long established fact that a reader will be distracted by the readable content...</p>
  <a>Read More</a>
</article>
<div class="btn dark" style="left:536px;top:3582px;width:127px;height:41px">View All</div>

<!-- footer & newsletter -->
<footer class="abs footer"></footer>
<section class="abs newsletter">
  <h2 style="position:absolute;left:74px;top:56px;font-size:30px;font-weight:800;color:#fff">NEWSLETTER SIGN UP</h2>
  <p style="position:absolute;left:74px;top:107px;font-size:12px;color:#fff">Insider updates on new products and services</p>
  <div style="position:absolute;left:76px;top:152px;width:306px;height:40px;background:#fff;border-radius:2px;font-size:11.5px;color:#777;display:flex;align-items:center;padding-left:22px">Enter Your Email Address</div>
  <div class="btn dark" style="left:389px;top:152px;width:125px;height:40px">Subscribe</div>
  <div style="position:absolute;left:580px;top:108px;display:flex;align-items:center;gap:14px;color:#fff;font-size:26px;font-weight:800">
    <span style="width:34px;height:34px;border-radius:50%;background:#fff"></span>TANDEM PARCEL
  </div>
</section>

<div class="abs" style="left:145px;top:4020px;color:#fff">
  <div style="font-size:22px;font-weight:800;display:flex;align-items:center;gap:10px"><span style="width:18px;height:18px;border-radius:50%;background:#dc0a0a"></span>TANDEM PARCEL</div>
  <div style="font-size:8px;letter-spacing:2.2px;font-weight:500;padding-left:28px;margin-top:2px">MAILBOXES | SHIPPING | NOTARY</div>
</div>
<div class="abs foot-social"><span></span><span></span><span></span><span></span></div>

<div class="footer-col" style="left:489px">
  <h4><span class="accent">QUICK</span> LINKS</h4>
  <ul><li>• Home</li><li>• About Us</li><li>• Services</li><li>• Estimates</li><li>• News</li><li>• Locations</li><li>• Contact Us</li></ul>
</div>
<div class="footer-col" style="left:656px">
  <h4><span class="accent">HOW</span> CAN WE HELP</h4>
  <ul><li>• Customer Service</li><li>• Estimate Shipping</li><li>• Find A Store</li><li>• FAQs</li></ul>
</div>
<div class="footer-col" style="left:877px">
  <h4><span class="accent">CONTACT</span> DETAILS</h4>
  <div class="contact-row"><svg width="16" height="20" viewBox="0 0 16 20"><path d="M8 1a6 6 0 00-6 6c0 5 6 11 6 11s6-6 6-11a6 6 0 00-6-6z" fill="none" stroke="#fff" stroke-width="1.6"/><circle cx="8" cy="7" r="2.2" fill="#fff"/></svg><span>123, Building Name, Street<br>City, State XY 123456</span></div>
  <div class="contact-row" style="margin-top:8px"><svg width="16" height="12" viewBox="0 0 16 12"><rect x=".8" y=".8" width="14.4" height="10.4" rx="1" fill="none" stroke="#fff" stroke-width="1.4"/><path d="M1 1l7 6 7-6" stroke="#fff" stroke-width="1.4" fill="none"/></svg><span>hello@tandemparcel.com</span></div>
  <div class="contact-row" style="margin-top:8px"><svg width="16" height="16" viewBox="0 0 24 24"><path d="M6.6 10.8a15 15 0 006.6 6.6l2.2-2.2c.3-.3.7-.4 1-.2 1.1.4 2.3.6 3.6.6.6 0 1 .4 1 1V20c0 .6-.4 1-1 1A17 17 0 013 4c0-.6.4-1 1-1h3.5c.6 0 1 .4 1 1 0 1.3.2 2.5.6 3.6.1.3 0 .7-.2 1z" fill="none" stroke="#fff" stroke-width="1.8"/></svg><span>(123) 456-7890</span></div>
</div>
<div class="abs copyright">©2024 Tandem Parcel. All Rights Reserved.</div>

</body>
</html>
```